Sports coaching website.

Hi there web designers,

We need a modern fully functional website to set us apart from our competition. The website will be information based with pictures and videos provided by us. The website must include members log in where they can pay for sessions directly online and subscribe to direct debit.

Target Market(s)

parents/teachers/schools/community/children.

Number of Pages Required

5+ page

Font styles to use
Sans Serif

Colors
acd037
3176b5
ffffff
000000
919191
f37122

Requirements
Must have
• Pictures, be modern, fully functional, must be clear, bold, e-basket, log-in.

```html
<!DOCTYPE html>
<html lang="en">
<head>
<meta charset="utf-8">
<title>Pacefield Sports – Sports Coaching</title>
<link rel="stylesheet" href="https://fonts.googleapis.com/css2?family=Open+Sans:wght@400;600;700&family=Roboto+Slab:wght@300;400;700&display=swap">
<style>
:root{
  --green:#acd037;
  --blue:#3176b5;
  --blue-dark:#2a67a0;
  --orange:#f37122;
  --grey:#919191;
  --text:#6b6b6b;
  --white:#ffffff;
  --black:#000000;
  --footer:#1e1e1e;
  --footer-bar:#111111;
  --heading:#2f6fae;
}
*{box-sizing:border-box;margin:0;padding:0}
html,body{width:1200px;height:2635px;overflow:hidden;background:var(--white)}
body{font-family:"Open Sans",Arial,sans-serif;color:var(--text);position:relative}
.slab{font-family:"Roboto Slab",Georgia,serif}
.abs{position:absolute}

/* header */
.site-header{position:absolute;left:0;top:0;width:1200px;height:112px;background:var(--white);z-index:3}
.brand{position:absolute;left:92px;top:22px;width:150px;height:128px;background:var(--white);display:flex;flex-direction:column;align-items:center;justify-content:center;gap:8px;z-index:4}
.brand-dot{width:44px;height:44px;border-radius:50%;background:var(--orange)}
.brand-name{font-family:"Roboto Slab",Georgia,serif;font-weight:700;font-size:17px;color:var(--black);text-align:center;line-height:1.1}
.header-tab{position:absolute;left:0;top:112px;width:262px;height:62px;background:var(--white);clip-path:polygon(0 0,100% 0,90% 100%,0 100%);z-index:2}
.search-btn{position:absolute;left:584px;top:22px;width:30px;height:30px;border-radius:50%;background:#eeeeee}
.social-label{position:absolute;left:634px;top:29px;font-size:11px;color:var(--grey)}
.social{position:absolute;top:24px;width:26px;height:26px;border-radius:50%}
.quote-btn{position:absolute;left:965px;top:20px;width:137px;height:35px;background:var(--green);color:var(--white);font-size:11.5px;font-weight:600;display:flex;align-items:center;justify-content:center;gap:6px;border-radius:2px}
.main-nav{position:absolute;top:74px;left:0;font-size:11.5px;font-weight:600;color:#333;text-transform:uppercase}
.main-nav span{position:absolute;white-space:nowrap}
.main-nav .active{color:var(--blue)}

/* hero */
.hero{position:absolute;left:0;top:112px;width:1200px;height:513px;background:linear-gradient(180deg,#7d9a6a 0%,#6f9150 45%,#5d8a3a 100%)}
.hero-photo{position:absolute;left:360px;top:0;width:840px;height:513px;background:radial-gradient(ellipse at 55% 55%,#b83232 0%,#a83a3a 30%,rgba(120,140,90,0) 70%)}
.hero-title{position:absolute;left:98px;top:185px;width:434px;height:143px;background:rgba(20,20,20,.72);padding:18px 18px}
.hero-title .kicker{font-family:"Roboto Slab",Georgia,serif;font-weight:300;font-size:36px;color:var(--green);text-align:center;line-height:1.1}
.hero-title h1{font-family:"Roboto Slab",Georgia,serif;font-weight:700;font-size:49px;color:var(--white);line-height:1.15}
.hero-arrow{position:absolute;top:236px;width:40px;height:40px;border-radius:50%;background:rgba(40,40,40,.75)}

/* what we do */
.intro-photo{position:absolute;left:102px;top:670px;width:296px;height:296px;border-radius:50%;background:linear-gradient(160deg,#d8c9a6,#8a6f4a 55%,#c9763c);border:6px solid #ededed}
.intro-title{position:absolute;left:473px;top:678px;font-family:"Roboto Slab",Georgia,serif;font-weight:700;font-size:30px;color:var(--heading)}
.intro-copy{position:absolute;left:473px;top:728px;width:630px;font-size:11.6px;line-height:25px;color:var(--grey)}
.intro-copy p+p{margin-top:13px}
.btn{position:absolute;height:40px;color:var(--white);font-family:"Roboto Slab",Georgia,serif;font-weight:700;font-size:11.5px;display:flex;align-items:center;justify-content:center;border-radius:2px}

/* testimonials */
.testimonials{position:absolute;left:0;top:1030px;width:1200px;height:465px;background:var(--blue)}
.section-title{position:absolute;left:0;width:1200px;text-align:center;font-family:"Roboto Slab",Georgia,serif;font-weight:700;font-size:28px}
.video{position:absolute;top:117px;width:316px;height:211px;border:3px solid var(--white)}
.video .bar{position:absolute;left:0;bottom:0;width:100%;height:24px;background:rgba(20,20,20,.7)}
.video .play{position:absolute;left:6px;bottom:4px;width:30px;height:16px;background:#333}
.video .track{position:absolute;left:44px;right:60px;bottom:10px;height:4px;background:#888}
.video .big-play{position:absolute;left:50%;top:44%;width:40px;height:40px;margin:-20px 0 0 -20px;border-radius:50%;background:rgba(255,255,255,.55)}
.quote{position:absolute;top:342px;width:316px;text-align:center;font-family:"Roboto Slab",Georgia,serif;font-style:italic;font-size:11.5px;line-height:24px;color:var(--white)}
.quote .mark{font-size:30px;color:#9cc0e4;vertical-align:-8px}
.quote .by{display:block;font-style:italic;color:var(--green);font-size:11px;line-height:22px}

/* services */
.services-title{top:1540px;color:var(--heading)}
.tile{position:absolute}
.tile .cap{position:absolute;left:0;bottom:0;width:100%;height:38px;background:rgba(49,118,181,.85);color:var(--white);font-size:14.5px;display:flex;align-items:center;justify-content:center}
.tile .cap.green{background:var(--green)}

/* events + images */
.events-band{position:absolute;left:0;top:1975px;width:1200px;height:405px;background:var(--orange)}
.band-title{position:absolute;top:52px;font-family:"Roboto Slab",Georgia,serif;font-weight:700;font-size:18px;color:var(--white)}
.event-date{position:absolute;left:98px;width:62px;height:62px;background:var(--green);color:var(--white);text-align:center;font-family:"Roboto Slab",Georgia,serif}
.event-date b{display:block;font-size:16px;padding-top:10px}
.event-date small{font-size:10px}
.event-body{position:absolute;left:187px;width:430px;font-family:"Roboto Slab",Georgia,serif;color:var(--white)}
.event-body h3{font-weight:400;font-size:12px;margin-bottom:6px}
.event-body p{font-size:11px;line-height:19px;color:#fde1cc}
.small-btn{position:absolute;height:30px;color:var(--white);font-family:"Roboto Slab",Georgia,serif;font-size:10.5px;display:flex;align-items:center;justify-content:center}
.gallery{position:absolute;left:665px;top:108px;width:437px;height:233px;background:var(--white);padding:2px;display:grid;grid-template-columns:1fr 1fr;grid-template-rows:1fr 1fr;gap:2px}

/* footer */
.site-footer{position:absolute;left:0;top:2380px;width:1200px;height:215px;background:var(--footer);color:#b5b5b5}
.footer-brand{position:absolute;left:98px;top:38px;width:134px;height:118px;display:flex;flex-direction:column;align-items:center;justify-content:center;gap:8px}
.footer-brand .brand-dot{background:#777}
.footer-brand .brand-name{color:#9a9a9a}
.footer-heading{position:absolute;top:42px;font-family:"Roboto Slab",Georgia,serif;font-weight:700;font-size:14px;color:var(--white)}
.footer-links{position:absolute;top:74px;font-size:11.5px;line-height:26px;color:#a8a8a8}
.newsletter-input{position:absolute;left:557px;top:78px;width:260px;height:38px;background:var(--white);font-size:11px;color:#777;padding:11px 10px;border-radius:2px}
.subscribe{position:absolute;left:557px;top:128px;width:113px;height:38px;background:var(--blue);color:var(--white);font-size:11px;display:flex;align-items:center;justify-content:center;border-radius:2px}
.contact-row{position:absolute;left:869px;font-size:11.5px;line-height:21px;color:#a8a8a8}
.contact-row svg{position:absolute;left:0;top:4px}
.contact-row span{display:block;padding-left:24px}
.footer-bar{position:absolute;left:0;top:2595px;width:1200px;height:40px;background:var(--footer-bar);color:#cfcfcf;font-size:11.5px;display:flex;align-items:center;justify-content:center}
</style>
</head>
<body>

<header class="site-header">
  <div class="search-btn"><svg width="30" height="30" viewBox="0 0 30 30"><circle cx="14" cy="14" r="4.5" fill="none" stroke="#999" stroke-width="1.5"/><line x1="17.5" y1="17.5" x2="20" y2="20" stroke="#999" stroke-width="1.5"/></svg></div>
  <div class="social-label">Connect with our social network :</div>
  <span class="social" style="left:816px;background:#3b5ba0"></span>
  <span class="social" style="left:850px;background:#2ea7e0"></span>
  <span class="social" style="left:884px;background:#f29b1f"></span>
  <span class="social" style="left:918px;background:#1a7bb0"></span>
  <div class="quote-btn">Request a Quote <svg width="8" height="10" viewBox="0 0 8 10"><path d="M2 1l4 4-4 4" fill="none" stroke="#fff" stroke-width="1.8"/></svg></div>
  <nav class="main-nav">
    <span class="active" style="left:367px">Home</span>
    <span style="left:449px">About PFS</span>
    <span style="left:558px">Schools</span>
    <span style="left:657px">Sessions</span>
    <span style="left:758px">Workshops</span>
    <span style="left:876px">Charity/Community</span>
    <span style="left:1048px">Contact</span>
  </nav>
</header>
<div class="header-tab"></div>
<div class="brand"><span class="brand-dot"></span><span class="brand-name">PACEFIELD<br>SPORTS</span></div>

<section class="hero" role="img" aria-label="Coach talking to a group of children in red football kits on a grass pitch">
  <div class="hero-photo"></div>
  <div class="hero-title">
    <div class="kicker">PACEFIELD</div>
    <h1>Sports Coaching</h1>
  </div>
  <span class="hero-arrow" style="left:24px"><svg width="40" height="40" viewBox="0 0 40 40"><path d="M23 14l-6 6 6 6" fill="none" stroke="#fff" stroke-width="2"/></svg></span>
  <span class="hero-arrow" style="left:1136px"><svg width="40" height="40" viewBox="0 0 40 40"><path d="M17 14l6 6-6 6" fill="none" stroke="#fff" stroke-width="2"/></svg></span>
</section>

<section class="what-we-do">
  <div class="intro-photo" role="img" aria-label="Group of children with coaches sitting in a school sports hall"></div>
  <h2 class="intro-title">What We Do</h2>
  <div class="intro-copy">
    <p>Dolores eos qui ratione voluptatem sequi nesciunt. Neque porro quisquam est, qui dolorem ipsum quia dolor sit amet, consectetur, adipisci velit, sed quia non numquamsequi nesciunt. Neque porro quisquam est, qui dolorem ipsum quia dolor sit amet, consectetur, adipisci velit, sed quia non numquam eius modi tempora incidunt...</p>
    <p>Aolores eos qui ratione voluptatem sequi nesciunt. Neque porro quisquam est, qui dolorem ipsum quia dolor sit amet, consectetur, adipisci velit, sed quia non numquamsequi nesciunt. Neque porro quisquam est, qui dolorem ipsum quia dolor sit amet, consectetur, adipisci velit, sed quia non numquam eius modi tempora incidunt...</p>
  </div>
  <a class="btn" style="left:473px;top:924px;width:129px;background:var(--green)">Read More Info</a>
  <a class="btn" style="left:611px;top:924px;width:127px;background:var(--orange)">Get Start Today</a>
</section>

<section class="testimonials">
  <h2 class="section-title" style="top:48px;color:var(--white)">Video Testimonials</h2>
  <div class="video" style="left:98px;background:linear-gradient(135deg,#e9eef0,#b9cfd6 50%,#7fb3c9)" role="img" aria-label="Video of a tennis coach with a young girl"><span class="big-play"></span><span class="bar"><span class="play"></span><span class="track"></span></span></div>
  <div class="video" style="left:442px;background:linear-gradient(180deg,#b89c7c,#8f6f52 55%,#c23a30)" role="img" aria-label="Video of a teacher with a class of children in a sports hall"><span class="big-play"></span><span class="bar"><span class="play"></span><span class="track"></span></span></div>
  <div class="video" style="left:786px;background:linear-gradient(135deg,#6f9a4e,#c8d6c0 50%,#e5e8e4)" role="img" aria-label="Video of a tennis coach sitting with a boy on court"><span class="big-play"></span><span class="bar"><span class="play"></span><span class="track"></span></span></div>
  <div class="quote" style="left:98px"><span class="mark">“</span> Nemo enim ipsam voluptatem quia voluptas sit aspe rnatur aut odit aut fugit, sed quia conse <span class="mark">”</span><span class="by">Posted By - Mark Ellery</span></div>
  <div class="quote" style="left:442px"><span class="mark">“</span> Nemo enim ipsam voluptatem quia voluptas sit aspe rnatur aut odit aut fugit, sed quia conse <span class="mark">”</span><span class="by">Posted By - Mark Ellery</span></div>
  <div class="quote" style="left:786px"><span class="mark">“</span> Nemo enim ipsam voluptatem quia voluptas sit aspe rnatur aut odit aut fugit, sed quia conse <span class="mark">”</span><span class="by">Posted By - Mark Ellery</span></div>
</section>

<section class="services">
  <h2 class="section-title services-title">Our Services</h2>
  <div class="tile" style="left:98px;top:1602px;width:271px;height:319px;background:linear-gradient(180deg,#9aa7a8,#5f7d44 45%,#2f5a2a)" role="img" aria-label="Boy in blue kit dribbling a football on an artificial pitch"><span class="cap green">Neque porro quisquam &nbsp;&gt;&gt;</span></div>
  <div class="tile" style="left:372px;top:1602px;width:363px;height:158px;background:linear-gradient(135deg,#d9cfc2,#8a6a52 60%,#c9b79e)" role="img" aria-label="Children sitting on a hall floor during a session"><span class="cap">Neque porro quisquam &nbsp;&gt;&gt;</span></div>
  <div class="tile" style="left:738px;top:1602px;width:364px;height:158px;background:linear-gradient(135deg,#8c6a3e,#c49a52 50%,#6b5434)" role="img" aria-label="Children holding footballs in a sports hall"><span class="cap">Neque porro quisquam &nbsp;&gt;&gt;</span></div>
  <div class="tile" style="left:372px;top:1764px;width:363px;height:157px;background:linear-gradient(180deg,#d8d3c6,#c23b30 55%,#7a6b58)" role="img" aria-label="Team of children in red shirts holding a trophy"><span class="cap">Neque porro quisquam &nbsp;&gt;&gt;</span></div>
  <div class="tile" style="left:738px;top:1764px;width:364px;height:157px;background:linear-gradient(180deg,#8fb070,#c8343a 50%,#5c8a3a)" role="img" aria-label="Football team in red celebrating on grass"><span class="cap">Neque porro quisquam &nbsp;&gt;&gt;</span></div>
</section>

<section class="events-band">
  <h2 class="band-title" style="left:98px">Upcoming Events</h2>
  <svg class="abs" style="left:596px;top:58px" width="28" height="12" viewBox="0 0 28 12"><circle cx="6" cy="6" r="5" fill="none" stroke="#fff" stroke-width="1.4"/><path d="M7 3.5L4.5 6 7 8.5" fill="none" stroke="#fff" stroke-width="1.4"/><circle cx="21" cy="6" r="5" fill="none" stroke="#fff" stroke-width="1.4"/><path d="M20 3.5L22.5 6 20 8.5" fill="none" stroke="#fff" stroke-width="1.4"/></svg>

  <div class="event-date" style="top:110px"><b>22</b><small>August</small></div>
  <div class="event-body" style="top:102px">
    <h3>Duis aute irure dolor in reprehenderit in voluptate velit esse cillum dolore</h3>
    <p>Voluptatem quia voluptas sit aspernatur aut odit aut fugit, sed quia consequuntur magni dolores eos qui ratione voluptatem sequi nesciunt...</p>
  </div>
  <a class="small-btn" style="left:187px;top:174px;width:113px;background:var(--blue)">Booking Now</a>
  <a class="small-btn" style="left:304px;top:174px;width:114px;background:var(--green)">More Information</a>

  <div class="event-date" style="top:244px"><b>22</b><small>August</small></div>
  <div class="event-body" style="top:236px">
    <h3>Duis aute irure dolor in reprehenderit in voluptate velit esse cillum dolore</h3>
    <p>Voluptatem quia voluptas sit aspernatur aut odit aut fugit, sed quia consequuntur magni dolores eos qui ratione voluptatem sequi nesciunt...</p>
  </div>
  <a class="small-btn" style="left:187px;top:308px;width:113px;background:var(--blue)">Booking Now</a>
  <a class="small-btn" style="left:304px;top:308px;width:114px;background:var(--green)">More Information</a>

  <h2 class="band-title" style="left:662px">Images</h2>
  <div class="gallery">
    <div style="background:linear-gradient(135deg,#8a6d42,#b7954f)" role="img" aria-label="Children with footballs in a sports hall"></div>
    <div style="background:linear-gradient(135deg,#a98a55,#6c5a3c)" role="img" aria-label="Coach and children playing in a sports hall"></div>
    <div style="background:linear-gradient(135deg,#b59a62,#7a6440)" role="img" aria-label="Children running drills in a sports hall"></div>
    <div style="background:linear-gradient(135deg,#9c7e4c,#d0b57a)" role="img" aria-label="Children playing a game in a gym"></div>
  </div>
</section>

<footer class="site-footer">
  <div class="footer-brand"><span class="brand-dot"></span><span class="brand-name">PACEFIELD<br>SPORTS</span></div>

  <h3 class="footer-heading" style="left:305px">Quick Links</h3>
  <div class="footer-links" style="left:305px">Home Page<br>About PFS<br>Schools<br>Sessions</div>
  <div class="footer-links" style="left:390px">Workshops<br>Charity/Community<br>Contact</div>

  <h3 class="footer-heading" style="left:557px">Newsletter</h3>
  <div class="newsletter-input">Enter E-mail Address</div>
  <div class="subscribe">SUBSCRIBE</div>

  <h3 class="footer-heading" style="left:869px">Contact Info</h3>
  <div class="contact-row" style="top:72px"><svg width="12" height="14" viewBox="0 0 12 14"><path d="M6 0a5 5 0 0 1 5 5c0 4-5 9-5 9S1 9 1 5a5 5 0 0 1 5-5z" fill="#a8a8a8"/><circle cx="6" cy="5" r="2" fill="#1e1e1e"/></svg><span>48 Meadowbank Lane, Fieldgate,<br>City-20417</span></div>
  <div class="contact-row" style="top:122px"><svg width="12" height="14" viewBox="0 0 12 14"><path d="M2 1l3 0 1 3-2 1.5c1 2 2 3 4 4L9.5 7.5l2.5 1v3c-6 1-11-4-10-10.5z" fill="#a8a8a8"/></svg><span>Phone : (+111) 555-0142</span></div>
  <div class="contact-row" style="top:148px"><svg width="14" height="14" viewBox="0 0 14 14"><rect x="1" y="3" width="12" height="9" fill="none" stroke="#a8a8a8" stroke-width="1.3"/><path d="M1 3l6 5 6-5" fill="none" stroke="#a8a8a8" stroke-width="1.3"/></svg><span>E-mail : hello@pacefieldsports.com</span></div>
</footer>
<div class="footer-bar">© 2016 . Pacefield Sports | Allrights Reserved.</div>

</body>
</html>
```